Fallow Crest Bourbon Barrel Aged Wine

We are taking a sweet red wine and barrel aging it in previously used bourbon barrels. The abv is 16%. Kentucky based. I have attached our Brand logo for reference. Use colors that evoke warmth, richness, and sophistication. We would like to consider a raised or textured label.

Target Market(s)

bourbon and wine drinkers

```html
<!DOCTYPE html>
<html lang="en">
<head>
<meta charset="utf-8">
<title>Fallow Crest Bourbon Barrel Aged Wine – Label</title>
<link rel="stylesheet" href="https://fonts.googleapis.com/css2?family=Cinzel:wght@500;700&family=Jost:wght@300;400&display=swap">
<style>
  :root {
    --page-bg: #f6f6f6;
    --label-cream: #fbf8f1;
    --label-cream-deep: #f3ecdc;
    --ink-navy: #3a3f78;
    --wine-red: #5a0d0d;
    --gold-light: #d9a93f;
    --gold-deep: #b9892a;
    --hill-sand: #eedfbf;
    --hill-sand-soft: #f5ecd8;
    --hill-sand-deep: #e4cf9f;
  }
  * { box-sizing: border-box; margin: 0; padding: 0; }
  html, body {
    width: 730px; height: 1200px; overflow: hidden;
    background: var(--page-bg);
  }
  .canvas {
    position: relative; width: 730px; height: 1200px;
    background: var(--page-bg);
  }
  .label {
    position: absolute; left: 25px; top: 110px;
    width: 680px; height: 980px; overflow: hidden;
    background: linear-gradient(180deg, var(--label-cream) 0%, var(--label-cream-deep) 100%);
    box-shadow: 0 1px 4px rgba(0,0,0,0.08);
  }
  .label-texture {
    position: absolute; inset: 0;
    background: linear-gradient(180deg, rgba(238,223,191,0.25), rgba(238,223,191,0.1));
  }
  .brand-seal {
    position: absolute; left: 254px; top: 14px;
    width: 172px; height: 172px; border-radius: 50%;
    background: radial-gradient(circle at 40% 35%, var(--gold-light), var(--gold-deep));
  }
  .brand-name {
    position: absolute; left: 0; right: 0; top: 208px;
    text-align: center;
    font-family: "Cinzel", serif; font-weight: 500;
    font-size: 50px; line-height: 1; color: var(--ink-navy);
    letter-spacing: 0.5px;
  }
  .rule-caption {
    position: absolute; left: 0; right: 0;
    display: flex; align-items: center; justify-content: center; gap: 14px;
    color: var(--ink-navy);
  }
  .rule-caption .rule { height: 2px; background: var(--ink-navy); }
  .brand-descriptor { top: 259px; }
  .brand-descriptor .rule { width: 106px; }
  .brand-descriptor span {
    font-family: "Cinzel", serif; font-weight: 500;
    font-size: 22px; letter-spacing: 2px; line-height: 1;
  }
  .wine-type {
    position: absolute; left: 0; right: 0; top: 468px;
    text-align: center;
    font-family: "Cinzel", serif; font-weight: 700;
    font-size: 60px; line-height: 1; color: var(--wine-red);
  }
  .origin { top: 527px; }
  .origin .rule { width: 48px; height: 1px; }
  .origin span {
    font-family: "Jost", sans-serif; font-weight: 400;
    font-size: 13px; letter-spacing: 8px; line-height: 1;
    padding-left: 8px;
  }
  .abv {
    position: absolute; left: 553px; top: 742px;
    color: var(--ink-navy); font-family: "Jost", sans-serif; font-weight: 300;
  }
  .abv-key { display: block; font-size: 10px; line-height: 1; }
  .abv-value { display: block; font-size: 30px; line-height: 1; }
  .hills { position: absolute; left: 0; bottom: 0; width: 680px; height: 150px; }
  .barrel-mark { position: absolute; left: 0; top: 720px; width: 680px; height: 190px; }
  .aging-note {
    position: absolute; top: 808px;
    font-family: "Jost", sans-serif; font-weight: 400;
    font-size: 15px; letter-spacing: 0.5px; color: var(--ink-navy); line-height: 1;
  }
  .aging-note--left { left: 93px; }
  .aging-note--right { left: 429px; }
  .vintage {
    position: absolute; left: 0; right: 0; top: 898px;
    text-align: center;
    font-family: "Jost", sans-serif; font-weight: 400;
    font-size: 24px; color: var(--ink-navy); line-height: 1;
  }
</style>
</head>
<body>
<main class="canvas">
  <section class="label">
    <div class="label-texture" role="img" aria-label="Fine horizontal textured paper grain"></div>

    <div class="brand-seal"></div>
    <h1 class="brand-name">Fallow Crest</h1>
    <div class="rule-caption brand-descriptor"><i class="rule"></i><span>Distillery</span><i class="rule"></i></div>

    <h2 class="wine-type">Red Wine</h2>
    <div class="rule-caption origin"><i class="rule"></i><span>KENTUCKY</span><i class="rule"></i></div>

    <div class="abv"><span class="abv-key">ABV</span><span class="abv-value">16%</span></div>

    <svg class="hills" viewBox="0 0 680 150" preserveAspectRatio="none" aria-hidden="true">
      <path d="M0 40 C120 10 220 30 330 20 C450 10 560 25 680 15 L680 150 L0 150 Z" fill="var(--hill-sand-soft)"/>
      <path d="M0 75 C140 55 260 80 380 62 C500 45 600 60 680 50 L680 150 L0 150 Z" fill="var(--hill-sand)"/>
      <path d="M0 115 C150 100 300 125 430 108 C540 95 620 108 680 100 L680 150 L0 150 Z" fill="var(--hill-sand-deep)" opacity="0.7"/>
    </svg>

    <svg class="barrel-mark" viewBox="0 0 680 190" aria-hidden="true">
      <line x1="91" y1="108" x2="254" y2="108" stroke="var(--ink-navy)" stroke-width="1.5"/>
      <line x1="426" y1="108" x2="584" y2="108" stroke="var(--ink-navy)" stroke-width="1.5"/>
      <circle cx="340" cy="94" r="84" fill="none" stroke="var(--ink-navy)" stroke-width="1.5"/>
      <circle cx="340" cy="94" r="76" fill="none" stroke="var(--ink-navy)" stroke-width="1"/>
    </svg>
    <svg class="barrel-mark" viewBox="0 0 680 190" role="img" aria-label="Illustration of stacked bourbon barrels">
      <circle cx="340" cy="94" r="52" fill="var(--ink-navy)" opacity="0.85"/>
    </svg>

    <span class="aging-note aging-note--left">BOURBON BARREL</span>
    <span class="aging-note aging-note--right">AGED RED WINE</span>

    <p class="vintage">2023</p>
  </section>
</main>
</body>
</html>
```